Guaranteed Job - Sleek Sexy Business Card UV Spot

Im looking for a sleek and sexy business card, that resembles elite or VIP status status.
our business is corinvale.example
you can view our products on there, but our main audience for handing out our cards will be for people in the hospitality industry, so it will need to impress high management and CEO of hotels and restaurants, bars, clubs etc...
the card features will have UV spot on both sides, 400gsm stock. standard size.
Artwork should be 86 x 54mm + 2mm bleed = 90 x 58mm
it should have a nice "unique" uv spot pattern that highlights the card, not a repeated pattern, theres no originality there, and it will be disregarded.
The written material will be:
Corin Vale Hospitality College (logo)
Tobin Marsh
Director
Phone: 1300 615 737
Mobile: 0455 817 296
Email: info@corinvale.example
website: www.corinvale.example
I'm looking for originality here, i don't want just a simple stock card, want something that has a wow factor for people.
You will find the logo attached. you may invert the white to black words to suit the background as you please.
thank you and good luck
As a side note, ive received a lot of proposals, im too busy to give feedback to each and every one, so if i havent provided feedback for your design within 24 hours, then consider it not acceptable, and you could resubmit another design.
So far i have not seen any design that stood out for me, they all seem pretty generic. there nothing thats unique, i would figure for the amount that im offering, that people would put some more effort and creativity into the design.
so far over 200 designs submitted, and nothing i have seen looks very original, everything looks like a different variation of the same stuff, i said it very clearly i wanted something unique, the only thing that has come close to it so far is this one
Reason: Ive received alot of design concepts and i have reviewed everyone, but i havent had time to give feedback to every single one, only the ones that have interested me, if i havent responded, its because i havent found it good enough.
so far only a few design have been on par with what ive been looking for, an attractive eye popping design.
heres a few of them,
http://files.pixelbazaar.example/design_img/51736/62418/62418_2840915_51736_image.jpg
http://files.pixelbazaar.example/design_img/51736/68254/68254_2841377_51736_image.jpg
theyre, both unique and original, and eye catching, the only thing theyre missing is the sexyness.
if you still think you have some creativity left in your minds, then throw it on here.
Reason: Sorry guys for the delay, I was in a serious accident and out of commission for the past few months, I'm just slowly recovering now, please bare with me as i try to attend to this project, it may take me awhile as I have other projects that are on standby, I'm not 100% at the moment, so im extending the deadline for 2 weeks right now. Thanks for your patience.
Hospitality

```html
<!DOCTYPE html>
<html lang="en">
<head>
<meta charset="utf-8">
<title>Corin Vale Hospitality College – Business Card Concepts</title>
<link href="https://fonts.googleapis.com/css2?family=Barlow+Condensed:wght@600&family=Arimo:wght@400;700&display=swap" rel="stylesheet">
<style>
  :root {
    --backdrop: #e9e4dc;
    --card-white: #ffffff;
    --brand-blue: #5aabdf;
    --ink: #111111;
    --ink-soft: #333333;
    --grey: #8c8c8c;
    --label: #111111;
  }
  * { box-sizing: border-box; margin: 0; padding: 0; }
  html, body { width: 1200px; height: 788px; overflow: hidden; }
  body {
    position: relative;
    background: var(--backdrop);
    font-family: "Arimo", Arial, sans-serif;
  }
  .view-label {
    position: absolute;
    font-family: "Arimo", Arial, sans-serif;
    font-size: 20px;
    color: var(--label);
    transform: translateX(-50%);
  }
  .card {
    position: absolute;
    width: 523px;
    height: 299px;
    overflow: hidden;
    box-shadow: 3px 4px 8px rgba(0,0,0,0.35);
  }
  .card--front { left: 52px; top: 74px; background: var(--card-white); border-radius: 4px 4px 26px 14px; }
  .card--back-white { left: 624px; top: 74px; background: var(--card-white); border-radius: 4px 30px 4px 30px; }
  .card--back-blue { left: 57px; top: 447px; background: var(--brand-blue); border-radius: 30px 4px 30px 4px; }
  .card--back-black { left: 624px; top: 445px; background: var(--ink); border-radius: 4px 30px 4px 30px; }

  .wordmark {
    position: absolute;
    display: flex;
    align-items: center;
    gap: 14px;
    font-family: "Barlow Condensed", "Arial Narrow", sans-serif;
    font-weight: 600;
    text-transform: uppercase;
    line-height: 0.95;
  }
  .wordmark__square { width: 46px; height: 46px; background: var(--brand-blue); flex: none; }
  .wordmark__name { display: block; font-size: 44px; letter-spacing: 0.5px; }
  .wordmark__sub { display: block; font-size: 19px; letter-spacing: 0.6px; }
  .wordmark--dark { color: var(--ink); }
  .wordmark--light { color: #ffffff; }
  .wordmark--large .wordmark__name { font-size: 58px; }
  .wordmark--large .wordmark__sub { font-size: 23px; }
  .wordmark--large .wordmark__square { width: 120px; height: 120px; background: #ffffff; }

  .contact {
    position: absolute;
    left: 328px;
    top: 54px;
    padding-left: 8px;
    border-left: 1.5px solid var(--ink-soft);
    font-size: 12.5px;
    color: var(--ink-soft);
    line-height: 22px;
  }
  .contact__name { font-size: 16px; color: var(--ink); }
  .contact__role { font-size: 13px; }
  .contact__key { font-weight: 700; font-style: italic; }

  .front-wave { position: absolute; left: 0; top: 0; }
  .address {
    position: absolute;
    left: 0; right: 0; bottom: 14px;
    text-align: center;
    font-size: 15px;
    color: #ffffff;
    letter-spacing: 0.3px;
  }
  .web {
    position: absolute;
    left: 0; right: 0; bottom: 14px;
    text-align: center;
    font-size: 12.5px;
    letter-spacing: 2.6px;
  }
  .web--dark { color: var(--ink-soft); }
  .web--light { color: #ffffff; }
  .card--back-blue .web { text-align: right; padding-right: 30px; bottom: 18px; }
</style>
</head>
<body>
  <span class="view-label" style="left:320px; top:36px;">Front</span>
  <span class="view-label" style="left:896px; top:36px;">Back - 1</span>
  <span class="view-label" style="left:324px; top:406px;">Back - 2</span>
  <span class="view-label" style="left:896px; top:406px;">Back - 3</span>

  <section class="card card--front">
    <svg class="front-wave" width="523" height="299" viewBox="0 0 523 299" aria-hidden="true">
      <path d="M0,262 C150,232 290,262 400,250 C460,243 505,222 523,188 L523,299 L0,299 Z" fill="var(--brand-blue)"/>
      <path d="M340,250 C430,248 500,222 523,156 L523,180 C505,228 440,250 340,250 Z" fill="var(--ink)"/>
    </svg>
    <div class="wordmark wordmark--dark" style="left:28px; top:62px;">
      <span class="wordmark__square"></span>
      <span>
        <span class="wordmark__name">Corin Vale</span>
        <span class="wordmark__sub">Hospitality College</span>
      </span>
    </div>
    <div class="contact">
      <div><span class="contact__name">Tobin Marsh,</span> <span class="contact__role">Director</span></div>
      <div><span class="contact__key">p</span> : 1300 615 737</div>
      <div><span class="contact__key">c</span> : 0455 817 296</div>
      <div><span class="contact__key">e</span> : info@corinvale.example</div>
      <div><span class="contact__key">w</span> : www.corinvale.example</div>
    </div>
    <p class="address">4/18 Harlow St, Kestrel Bay, NSW</p>
  </section>

  <section class="card card--back-white">
    <div class="wordmark wordmark--dark" style="left:88px; top:96px;">
      <span class="wordmark__square" style="width:60px;height:60px;"></span>
      <span>
        <span class="wordmark__name" style="font-size:52px;">Corin Vale</span>
        <span class="wordmark__sub" style="font-size:21px;">Hospitality College</span>
      </span>
    </div>
    <p class="web web--dark">www.corinvale.example</p>
  </section>

  <section class="card card--back-blue">
    <div class="wordmark wordmark--light wordmark--large" style="left:60px; top:90px;">
      <span class="wordmark__square"></span>
      <span>
        <span class="wordmark__name">Corin Vale</span>
        <span class="wordmark__sub">Hospitality College</span>
      </span>
    </div>
    <p class="web web--light">www.corinvale.example</p>
  </section>

  <section class="card card--back-black">
    <div class="wordmark wordmark--light" style="left:88px; top:96px;">
      <span class="wordmark__square" style="width:60px;height:60px;"></span>
      <span>
        <span class="wordmark__name" style="font-size:52px;">Corin Vale</span>
        <span class="wordmark__sub" style="font-size:21px;">Hospitality College</span>
      </span>
    </div>
    <p class="web web--light">www.corinvale.example</p>
  </section>
</body>
</html>
```